New fresh design for ShopVantly Golf website

GOLF ECOMMERCE - We have had a new logo designed which we are happy with and now want this new theme rolled out across our ShopVantly store, Qivo Shop Template, Plinkora - Exciting modern, fresh design required with excellent menu presentation and ease of use the key priorities. Ongoing, I am looking for regular banner updates. I have attached our new logo designs so you can get a feel of the look.

Target Market(s)

UK Golfers

Industry/Entity Type

Store

Font styles to use
Sans Serif

Colors
0455a3
f37122
33a6d7
eaf1f7

Requirements
Must have
• Workable easy to read menu structure. Room for banners and Tandoro.co.uk widget. Social visibility icons

```html
<!DOCTYPE html>
<html lang="en">
<head>
<meta charset="utf-8">
<title>Fairwix Golf – Home</title>
<link href="https://fonts.googleapis.com/css2?family=Montserrat:wght@400;600;700&family=Open+Sans:wght@400;600;700&display=swap" rel="stylesheet">
<style>
:root{
  --navy:#0455a3;
  --orange:#f37122;
  --sky:#33a6d7;
  --mist:#eaf1f7;
  --ink:#333;
  --grey:#777;
  --line:#e3e7ec;
  --white:#fff;
}
*{box-sizing:border-box;margin:0;padding:0}
html,body{width:1200px;height:3475px;overflow:hidden}
body{position:relative;background:var(--white);font-family:"Open Sans",Arial,sans-serif;color:var(--ink)}
.abs{position:absolute}

/* header */
.site-header{top:0;left:0;width:1200px;height:104px}
.brand-name{left:111px;top:28px;font-family:"Montserrat",sans-serif;font-weight:700;font-size:36px;color:var(--navy);letter-spacing:-.5px}
.acct{top:36px;height:26px;display:flex;align-items:center;font-size:11.5px;color:var(--navy);white-space:nowrap}
.acct.signin{background:var(--mist);padding:0 12px;border-radius:2px}
.acct.cart{background:var(--navy);color:var(--white);padding:0 12px;border-radius:2px;font-size:12.5px}
.ico{display:inline-block;width:9px;height:9px;background:var(--navy);margin-right:6px;border-radius:2px}
.call{left:950px;top:24px;color:var(--orange);white-space:nowrap}
.call small{display:block;font-size:12px}
.call strong{font-family:"Montserrat",sans-serif;font-size:23px;font-weight:600}

/* nav */
.main-nav{top:104px;left:0;width:1200px;height:51px;background:#f1f4f7;border-top:1px solid var(--line);border-bottom:1px solid var(--line);display:flex;align-items:center;font-size:14px;color:var(--navy)}
.shop-all{margin-left:100px;width:148px;height:51px;background:var(--orange);color:var(--white);font-family:"Montserrat",sans-serif;font-size:15px;display:flex;align-items:center;justify-content:center;gap:18px}
.main-nav ul{list-style:none;display:flex;gap:26px;margin-left:18px}

/* hero */
.hero{top:155px;left:0;width:1200px;height:429px;background:linear-gradient(180deg,#d9e7c6 0%,#a9c788 45%,#5f9a3a 75%,#3f7a26 100%)}
.hero-copy{top:137px;width:1200px;text-align:center;color:#3a3a3a}
.hero-copy h1{font-family:"Montserrat",sans-serif;font-weight:400;font-size:38px;letter-spacing:2px}
.hero-copy p{font-size:16px;letter-spacing:1.5px;margin-top:10px}
.dots{display:flex;gap:10px;justify-content:center}
.dots i{width:10px;height:10px;border-radius:50%;background:var(--white);opacity:.9}
.hero .dots{position:absolute;top:389px;width:1200px}

/* section titles */
.section-title{width:1200px;text-align:center;font-family:"Montserrat",sans-serif;font-weight:600;font-size:26px;color:var(--orange)}

/* brands */
.brand-box{top:665px;width:107px;height:102px;border:1px solid var(--line);display:flex;align-items:center;justify-content:center;font-family:"Montserrat",sans-serif;font-weight:700;font-size:15px;color:#222}
.brands-rule{top:812px;left:0;width:1200px;height:1px;background:var(--line)}
.more-brands{top:813px;left:533px;width:139px;height:26px;background:var(--mist);font-size:11px;font-weight:600;color:var(--navy);display:flex;align-items:center;justify-content:center}

/* specials */
.timeline{top:995px;left:599px;width:2px;height:1530px;background:#edf0f3}
.step{width:52px;height:52px;border-radius:50%;left:574px;display:flex;align-items:center;justify-content:center;font-family:"Montserrat",sans-serif;font-size:22px}
.step.is-first{background:var(--sky);color:var(--white)}
.step.is-muted{background:#eceff3;color:#555}
.photo{width:397px;height:195px}
.special-text{width:380px;text-align:center}
.special-text h3{font-family:"Montserrat",sans-serif;font-weight:600;font-size:21px;color:var(--sky);letter-spacing:.5px}
.special-text .kicker{font-size:12px;font-weight:700;margin-top:9px}
.special-text .deal{font-family:"Montserrat",sans-serif;font-size:22px;font-weight:600;color:var(--navy);margin-top:9px}
.special-text .sale{font-size:14px;font-weight:600;color:#444;margin-top:4px}
.special-text .blurb{font-size:12.5px;line-height:20px;color:var(--grey);margin:10px auto 0;width:360px}
.special-text .more{font-size:11px;font-weight:700;color:var(--orange);margin-top:14px}

/* featured */
.featured{top:2595px;left:0;width:1200px;height:470px;background:var(--sky)}
.featured .section-title{position:absolute;top:30px;color:var(--white)}
.product{top:88px;width:218px;height:285px;background:var(--white)}
.product .shot{height:185px;background:linear-gradient(180deg,#fafafa,#e9ecef)}
.product .name{height:63px;display:flex;align-items:center;justify-content:center;text-align:center;padding:0 14px;font-size:11.5px;font-weight:700;line-height:15px;color:#333}
.product .bar{height:37px;background:var(--navy);color:var(--white);display:flex;justify-content:space-between;align-items:center;padding:0 14px;font-size:14px}
.product .bar b{font-size:11px}
.featured .dots{position:absolute;top:433px;width:1200px}
.featured .dots i{background:var(--white)}
.featured .dots i:first-child{background:var(--navy)}

/* footer */
.site-footer{top:3065px;left:0;width:1200px;height:364px;background:var(--mist)}
.col{top:30px}
.col h4{font-family:"Montserrat",sans-serif;font-weight:600;font-size:17px;color:var(--navy);margin-bottom:12px}
.col ul{list-style:none;font-size:11.5px;line-height:20.4px;color:#333}
.pay{display:flex;gap:9px}
.pay span{width:48px;height:32px;border-radius:3px;background:var(--white);border:1px solid #c9d2dc}
.badges{display:flex;gap:30px;margin-top:32px}
.badges span{height:28px;background:#d4dbe3;border-radius:14px}
.social{list-style:none;font-size:13px;color:#333}
.social li{display:flex;align-items:center;gap:14px;height:44px}
.social li i{width:37px;height:37px;border-radius:2px}
.legal{top:3429px;left:0;width:1200px;height:46px;background:#dde6ef;font-size:12px;color:#555;display:flex;align-items:center;justify-content:center}
.legal .code{position:absolute;right:50px}
</style>
</head>
<body>

<header class="site-header abs">
  <div class="brand-name abs">Fairwix Golf</div>
  <span class="acct signin abs" style="left:382px"><span class="ico"></span>Sign in or Create an account</span>
  <span class="acct abs" style="left:584px"><span class="ico"></span>My Account</span>
  <span class="acct abs" style="left:688px"><span class="ico"></span>My Favorites</span>
  <span class="acct cart abs" style="left:800px">My Cart : Item (0)</span>
  <div class="call abs">
    <small>
      <svg width="10" height="10" viewBox="0 0 10 10" style="margin-right:6px"><path d="M2 1l2 2-1 1.5a6 6 0 0 0 2.5 2.5L7 6l2 2-1.5 1.5C4 9 1 6 .5 2z" fill="#f37122"/></svg>Call Us
    </small>
    <strong>01632 960418</strong>
  </div>
</header>

<nav class="main-nav abs">
  <div class="shop-all">SHOP ALL <svg width="10" height="6" viewBox="0 0 10 6"><path d="M0 0h10L5 6z" fill="#fff"/></svg></div>
  <ul>
    <li>Popular:</li>
    <li>Recycled Golf Balls</li>
    <li>Special Offers</li>
    <li>Golf Day Discounts</li>
    <li>Cleats &amp; Spikes</li>
    <li>Golf Tees</li>
    <li>Golf Bags</li>
  </ul>
</nav>

<section class="hero abs" role="img" aria-label="Golf driver addressing a ball on a tee over a green fairway">
  <div class="hero-copy abs">
    <h1>NEQUE PORRO QUISQUAM EST</h1>
    <p>QUI DOLOREM IPSUM QUIA DOLOR SIT</p>
  </div>
  <div class="dots"><i></i><i></i><i></i><i></i></div>
</section>

<h2 class="section-title abs" style="top:595px">POPULAR BRANDS</h2>
<svg class="abs" style="left:176px;top:690px" width="22" height="50" viewBox="0 0 22 50"><path d="M20 1L2 25l18 24" fill="none" stroke="#9fc7e6" stroke-width="2"/></svg>
<div class="brand-box abs" style="left:283px">Oakmere</div>
<div class="brand-box abs" style="left:415px">Harlow</div>
<div class="brand-box abs" style="left:549px">Veltro</div>
<div class="brand-box abs" style="left:681px">Pinecrest</div>
<div class="brand-box abs" style="left:813px">Brackwood</div>
<svg class="abs" style="left:990px;top:690px" width="22" height="50" viewBox="0 0 22 50"><path d="M2 1l18 24L2 49" fill="none" stroke="#9fc7e6" stroke-width="2"/></svg>
<div class="brands-rule abs"></div>
<div class="more-brands abs">MORE BRANDS</div>

<h2 class="section-title abs" style="top:893px">STORE SPECIALS</h2>
<div class="timeline abs"></div>

<div class="step is-first abs" style="top:949px">1</div>
<div class="special-text abs" style="left:141px;top:1018px">
  <h3>GOLF DAY DISCOUNTS</h3>
  <div class="kicker">Store Specials</div>
  <div class="deal">Upto 25% OFF</div>
  <div class="sale">Select items on sale</div>
  <p class="blurb">Neque porro quisquam est, qui dolorem ipsum quia dolor sit amet, consectetur, adipisci velit, sed quia non numquam eius modi tempora incidun</p>
  <div class="more">LEARN MORE</div>
</div>
<div class="photo abs" style="left:651px;top:1024px;background:linear-gradient(160deg,#f2e7c9,#c9b27a 50%,#6f8f3f)" role="img" aria-label="Golfer finishing a swing against a sunlit course"></div>

<div class="step is-muted abs" style="top:1285px">2</div>
<div class="photo abs" style="left:151px;top:1337px;background:linear-gradient(180deg,#4f7d3c,#7fb05a 60%,#9cc36a)" role="img" aria-label="Couple walking the fairway carrying golf bags"></div>
<div class="special-text abs" style="left:697px;top:1322px">
  <h3>ESSENTIAL ACCESSORIES</h3>
  <div class="kicker">Store Specials</div>
  <div class="deal">Upto 20% OFF</div>
  <div class="sale">Select items on sale</div>
  <p class="blurb">Neque porro quisquam est, qui dolorem ipsum quia dolor sit amet, consectetur, adipisci velit, sed quia non numquam eius modi tempora incidun</p>
  <div class="more">LEARN MORE</div>
</div>

<div class="step is-muted abs" style="top:1591px">3</div>
<div class="special-text abs" style="left:141px;top:1639px">
  <h3>CLEATS &amp; SPIKES</h3>
  <div class="kicker">Store Specials</div>
  <div class="deal">Upto 20% OFF</div>
  <div class="sale">Select items on sale</div>
  <p class="blurb">Neque porro quisquam est, qui dolorem ipsum quia dolor sit amet, consectetur, adipisci velit, sed quia non numquam eius modi tempora incidun</p>
  <div class="more">LEARN MORE</div>
</div>
<div class="photo abs" style="left:658px;top:1636px;background:linear-gradient(180deg,#2f8fd6,#8ac6e8 45%,#4f8b3a 70%,#2e5a25)" role="img" aria-label="Golf shoe sole with cleats over a lakeside course"></div>

<div class="step is-muted abs" style="top:1888px">4</div>
<div class="photo abs" style="left:148px;top:1953px;background:linear-gradient(90deg,#d8d8d2,#8fbf55 45%,#6aa23d)" role="img" aria-label="Bag of plastic golf tees beside a red tee on grass"></div>
<div class="special-text abs" style="left:697px;top:1934px">
  <h3>GOLF TEES</h3>
  <div class="kicker">Store Specials</div>
  <div class="deal">Upto 20% OFF</div>
  <div class="sale">Select items on sale</div>
  <p class="blurb">Neque porro quisquam est, qui dolorem ipsum quia dolor sit amet, consectetur, adipisci velit, sed quia non numquam eius modi tempora incidun</p>
  <div class="more">LEARN MORE</div>
</div>

<div class="step is-muted abs" style="top:2221px">5</div>
<div class="special-text abs" style="left:141px;top:2293px">
  <h3>GOLF BAG DEALS</h3>
  <div class="kicker">Store Specials</div>
  <div class="deal">Upto 20% OFF</div>
  <div class="sale">Select items on sale</div>
  <p class="blurb">Neque porro quisquam est, qui dolorem ipsum quia dolor sit amet, consectetur, adipisci velit, sed quia non numquam eius modi tempora incidun</p>
  <div class="more">LEARN MORE</div>
</div>
<div class="photo abs" style="left:656px;top:2308px;background:linear-gradient(160deg,#2b3a1c,#c99a3a 40%,#e8c06a 55%,#4d6a28)" role="img" aria-label="Golfer swinging at sunset beside a golf bag"></div>

<section class="featured abs">
  <h2 class="section-title">FEATURED PRODUCTS</h2>
  <div class="product abs" style="left:118px">
    <div class="shot" role="img" aria-label="Golf bag strong arm support rod"></div>
    <div class="name">NEW Golf Bag Strong Arm Club Protector For Travelling</div>
    <div class="bar"><span>£16.99</span><b>SHOP NOW</b></div>
  </div>
  <div class="product abs" style="left:366px">
    <div class="shot" role="img" aria-label="Black golf grip training aid"></div>
    <div class="name">NEW Golf Grip Training Aid - Can Be Used On Any Club In The Golfers Bag</div>
    <div class="bar"><span>£14.99</span><b>SHOP NOW</b></div>
  </div>
  <div class="product abs" style="left:614px">
    <div class="shot" role="img" aria-label="Blue golf glove"></div>
    <div class="name">NEW Nilgrip Mens Universal One Size Fits All Golf Glove - LH - Blue</div>
    <div class="bar"><span>£9.95</span><b>SHOP NOW</b></div>
  </div>
  <div class="product abs" style="left:864px">
    <div class="shot" role="img" aria-label="White microfibre golf towel"></div>
    <div class="name">NEW DryPro Microfibre Golf Towel in White with Black Trim</div>
    <div class="bar"><span>£7.50</span><b>SHOP NOW</b></div>
  </div>
  <div class="dots"><i></i><i></i><i></i><i></i></div>
</section>

<footer class="site-footer abs">
  <div class="col abs" style="left:130px">
    <h4>Company</h4>
    <ul>
      <li>Home</li><li>About us</li><li>Blog</li><li>Shipping</li><li>Returns</li><li>Grading</li><li>Contact us</li><li>Tandoro.co.uk</li><li>Our Guarantee</li><li>Free Stuff</li><li>Privacy Policy</li><li>Cookie Policy</li><li>Install a GripMax Grip</li><li>SnapLid</li>
    </ul>
  </div>
  <div class="col abs" style="left:399px">
    <h4>Shop</h4>
    <ul>
      <li>OFFERS</li><li>Accessories</li><li>Bags &amp; Covers</li><li>Gloves &amp; Mitts</li><li>Grips</li><li>Balls</li><li>Recycled Golf Balls</li><li>Junior Products</li><li>Ladies Products</li><li>Tees</li><li>Training &amp; Practice</li><li>Trolleys &amp; Carts</li><li>Wet &amp; Winter</li><li>Workshop</li>
    </ul>
  </div>
  <div class="col abs" style="left:598px">
    <h4>Payments &amp; Security</h4>
    <div class="pay"><span></span><span></span><span></span><span></span></div>
    <div class="badges"><span style="width:50px"></span><span style="width:98px"></span></div>
  </div>
  <div class="col abs" style="left:892px">
    <h4>Social Media</h4>
    <ul class="social">
      <li><i style="background:#2d4f8f"></i>Plinkora</li>
      <li><i style="background:#3aa6dd"></i>Chirpa</li>
      <li><i style="background:#6d6f73"></i>Glimmo</li>
      <li><i style="background:#d9393f"></i>Pinvora</li>
      <li><i style="background:#c9281f"></i>Vidnest</li>
    </ul>
  </div>
</footer>

<div class="legal abs">© 2015 Fairwix Golf Ltd. Sitemap<span class="code">M1</span></div>

</body>
</html>
```